Create a website in Wordpress for an interior design company

Create a website for our interior design company 'Dwellora'

-Color preferences - Neutral and warm colors. Nothing too bright
-Aesthetic: Modern, Minimalist, Classic, Mature, Luxury
-Mission Statement: Transforming homes into personalized dream spaces through exceptional interior design, meticulous attention to detail, and a touch of the unexpected.
-Brand Values: innovation, creativity, passion and sustainability

Examples: https://www.petrakinslowinteriors.com.au/
https://www.tavelcraftstudio.com/

About
Portfolio
Inquire page

```html
<!DOCTYPE html>
<html lang="en">
<head>
<meta charset="utf-8">
<title>Dwellora — Interior Design</title>
<link href="https://fonts.googleapis.com/css2?family=Playfair+Display:ital,wght@0,400;0,500;0,600;0,700;1,700;1,800&family=Montserrat:wght@400;500;700;800&display=swap" rel="stylesheet">
<style>
:root{
  --bg:#f7ede3;
  --brown:#b98461;
  --gold:#b8975a;
  --ink:#1b1714;
  --text:#3b3430;
  --white:#ffffff;
  --band:#e3c9ad;
}
*{margin:0;padding:0;box-sizing:border-box}
html,body{width:1200px;height:4059px;overflow:hidden}
body{background:var(--bg);font-family:"Playfair Display",serif;color:var(--ink);position:relative}
.abs{position:absolute}
.topline{left:0;top:0;width:1200px;height:6px;background:var(--brown)}
.header{left:0;top:6px;width:1200px;height:96px;background:var(--white)}
.brand{font-family:"Montserrat",sans-serif;font-weight:800;color:var(--brown);letter-spacing:1px}
.header .brand{left:100px;top:36px;font-size:22px}
.nav{top:38px;font-size:17px;color:var(--text)}
.nav.active{color:var(--gold)}
.btn{background:var(--brown);color:var(--white);font-family:"Playfair Display",serif;font-weight:700;border-radius:30px;display:flex;align-items:center;justify-content:center}
.header .btn{left:962px;top:30px;width:139px;height:44px;font-size:17px}
.photo{display:block}
.hero-a{left:0;top:102px;width:400px;height:515px;background:linear-gradient(160deg,#d9d2c9,#8d8379 60%,#4a4540)}
.hero-b{left:400px;top:102px;width:400px;height:515px;background:linear-gradient(180deg,#9c9a96,#6d7378 55%,#3d3f42)}
.hero-c{left:800px;top:102px;width:400px;height:515px;background:linear-gradient(200deg,#efe3dc,#e6d6cd 60%,#cbbdb4)}
.welcome{left:400px;top:255px;width:400px;text-align:center;color:var(--white);font-size:26px}
.hero-title{left:400px;top:272px;width:400px;text-align:center;color:var(--white);font-size:92px;font-style:italic;font-weight:800;line-height:1.2}
.hero .btn,.hero-btn{left:501px;top:383px;width:200px;height:42px;font-size:17px}
.heading{font-size:46px;font-weight:600;text-transform:uppercase;letter-spacing:-.5px}
.heading span{color:var(--gold);font-weight:400}
.rule{height:2px;background:var(--brown)}
.about-text{left:99px;top:790px;width:495px;font-size:15.5px;line-height:25.7px;color:var(--text)}
.about-circle{left:642px;top:705px;width:448px;height:448px;border-radius:50%;background:var(--brown);opacity:.35}
.about-photo{left:642px;top:705px;width:440px;height:440px;border-radius:50%;background:radial-gradient(circle at 45% 40%,#f1ebe3,#c9b8a3 55%,#6f5d4b)}
.band{left:96px;width:1008px;height:22px;background:var(--band);opacity:.6}
.card{top:1438px;height:357px}
.card-title{color:var(--white);font-size:24px;font-weight:600}
.card-copy{font-family:"Montserrat",sans-serif;font-size:12px;line-height:20px;color:var(--white)}
.tab{top:2030px;font-size:21px}
.grid-img{width:326px;height:283px}
.blog-img{width:482px;height:280px;border-radius:0 70px 0 0}
.blog-body{width:482px;height:162px;background:var(--white);border-radius:70px 0 70px 0;box-shadow:0 6px 18px rgba(0,0,0,.05)}
.date{height:44px;width:148px;border-radius:24px;background:var(--brown);color:var(--white);font-family:"Montserrat",sans-serif;font-weight:500;font-size:15px;display:flex;align-items:center;justify-content:center}
.blog-title{font-size:26px;font-weight:600;line-height:34px}
.read{font-size:17px;font-weight:600;color:var(--gold)}
.foot-h{font-size:25px;font-weight:600}
.foot-s{font-family:"Montserrat",sans-serif;font-size:12.5px;color:var(--ink);line-height:18px}
.link{font-family:"Montserrat",sans-serif;font-size:14.5px;display:flex;align-items:center;gap:14px}
.link::before{content:"";width:9px;height:9px;border-radius:50%;background:var(--brown)}
.field{left:679px;width:387px;height:45px;background:var(--white);border-radius:4px;font-family:"Montserrat",sans-serif;font-size:14px;padding:13px 20px}
.social{top:3985px;width:30px;height:30px;border:1.5px solid var(--ink);border-radius:50%}
</style>
</head>
<body>
<div class="abs topline"></div>
<header class="abs header">
  <div class="abs brand">DWELLORA</div>
  <div class="abs nav active" style="left:578px">Home</div>
  <div class="abs nav" style="left:671px">About</div>
  <div class="abs nav" style="left:755px">Portfolio</div>
  <div class="abs nav" style="left:860px">Inquiry</div>
  <div class="abs btn">Contact Us</div>
</header>

<section class="hero">
  <div class="abs photo hero-a" role="img" aria-label="Living room with white sofa, armchair and piano"></div>
  <div class="abs photo hero-b" role="img" aria-label="Modern kitchen with bar stools and pendant lights"></div>
  <div class="abs photo hero-c" role="img" aria-label="Minimal bathroom with framed artwork and tall vase"></div>
  <div class="abs welcome">Welcome To</div>
  <div class="abs hero-title">Dwellora</div>
  <div class="abs btn hero-btn">Get a Consultation</div>
</section>

<section class="about">
  <h2 class="abs heading" style="left:99px;top:705px">About <span>Us</span></h2>
  <div class="abs rule" style="left:99px;top:765px;width:68px"></div>
  <p class="abs about-text">Sed ut perspiciatis unde omnis iste natus error sit voluptatem accusantium doloremque laudantium, totam rem aperiam, eaque ipsa quae ab illo inventore veritatis et quasi architecto beatae vitae dicta sunt explicabo. Nemo enim ipsam voluptatem quia voluptas sit aspernatur aut odit aut fugit, sed quia consequuntur magni dolores eos qui ratione voluptatem sequi nesciunt. Neque porro quisquam est, qui dolorem ipsum quia dolor sit amet, consectetur, adipisci velit, sed quia non numquam eius modi tempora incidunt ut labore et dolore magnam aliquam quaerat voluptatem.</p>
  <div class="abs btn" style="left:100px;top:1050px;width:151px;height:43px;font-size:17px">READ MORE</div>
  <div class="abs about-circle"></div>
  <div class="abs photo about-photo" role="img" aria-label="Bright kitchen with island, pendant lights and wood floor"></div>
</section>

<div class="abs band" style="top:1236px"></div>

<section class="services">
  <h2 class="abs heading" style="left:0;width:1200px;text-align:center;top:1323px">Our <span>Services</span></h2>
  <div class="abs rule" style="left:565px;top:1384px;width:68px"></div>
  <div class="abs card photo" style="left:99px;width:320px;background:linear-gradient(180deg,#b9b0a6,#6e655d 50%,#241f1b)" role="img" aria-label="Apartment dining area with grand piano"></div>
  <div class="abs card-title" style="left:115px;top:1648px">Apartment Design</div>
  <p class="abs card-copy" style="left:115px;top:1692px;width:270px">Sed ut perspiciatis unde omnis iste natus error sit voluptatem accusantium doloremque laudantium,</p>
  <div class="abs" style="left:116px;top:1765px;color:var(--white);font-size:13px;font-weight:700;text-decoration:underline">LEARN MORE</div>
  <div class="abs card photo" style="left:439px;width:322px;background:linear-gradient(180deg,#e6e4e1,#c8c3bd 60%,#a99a8a)" role="img" aria-label="Home gym with treadmill under a skylight"></div>
  <div class="abs card-title" style="left:456px;top:1733px;font-size:21px">Architectural Design</div>
  <div class="abs card photo" style="left:780px;width:321px;background:linear-gradient(180deg,#d6d9dc,#8e9094 50%,#c6c3be)" role="img" aria-label="Modern house exterior with garage and driveway"></div>
  <div class="abs card-title" style="left:797px;top:1733px;font-size:21px">Office Design</div>
  <div class="abs card photo" style="left:1123px;width:77px;background:linear-gradient(180deg,#9aa39a,#6b6258 55%,#a58663)" role="img" aria-label="Outdoor patio with fire pit and lit house"></div>
  <div class="abs card-title" style="left:1140px;top:1733px;font-size:21px">Lighting</div>
</section>

<div class="abs band" style="top:1915px"></div>

<section class="portfolio">
  <h2 class="abs heading" style="left:101px;top:2013px">Our <span>Portfolio</span></h2>
  <div class="abs rule" style="left:101px;top:2073px;width:68px"></div>
  <div class="abs tab" style="left:701px;color:var(--brown);text-decoration:underline;text-underline-offset:6px">Bathrooms</div>
  <div class="abs tab" style="left:862px">kitchens</div>
  <div class="abs" style="left:1014px;top:2034px;font-size:17px">View All &raquo;</div>
  <div class="abs photo grid-img" style="left:99px;top:2136px;background:linear-gradient(160deg,#e4e1dd,#b9a995 60%,#7aa0b3)" role="img" aria-label="Playroom with colourful floor mat"></div>
  <div class="abs photo grid-img" style="left:438px;top:2136px;background:linear-gradient(180deg,#a7a3a7,#585249 55%,#4f7a3e)" role="img" aria-label="Pool house at dusk with lit windows"></div>
  <div class="abs photo grid-img" style="left:776px;top:2136px;background:linear-gradient(160deg,#d8d2cb,#eeebe7 50%,#a08a73)" role="img" aria-label="Hallway with round mirror and wood floor"></div>
  <div class="abs photo grid-img" style="left:99px;top:2433px;background:linear-gradient(170deg,#e8e6e3,#c9c2b8 60%,#9c8b78)" role="img" aria-label="Living room with white sofa and large windows"></div>
  <div class="abs photo grid-img" style="left:438px;top:2433px;background:linear-gradient(160deg,#d9d9d8,#9f9b97 50%,#4b3c31)" role="img" aria-label="Outdoor air hockey table on mulch"></div>
  <div class="abs photo grid-img" style="left:776px;top:2433px;background:linear-gradient(180deg,#b7cfe6,#dcdad6 50%,#6a8a4a)" role="img" aria-label="White brick house facade with trees"></div>
</section>

<div class="abs band" style="top:2818px"></div>

<section class="blog">
  <h2 class="abs heading" style="left:0;width:1200px;text-align:center;top:2917px">Our <span>Blog</span></h2>
  <div class="abs rule" style="left:566px;top:2977px;width:68px"></div>
  <svg class="abs" style="left:26px;top:3209px" width="40" height="40" viewBox="0 0 40 40" aria-hidden="true"><circle cx="20" cy="20" r="18" fill="none" stroke="#1b1714" stroke-width="2"/><path d="M29 20H11M17 14l-6 6 6 6" fill="none" stroke="#1b1714" stroke-width="2" stroke-linecap="round" stroke-linejoin="round"/></svg>
  <svg class="abs" style="left:1119px;top:3228px" width="40" height="40" viewBox="0 0 40 40" aria-hidden="true"><circle cx="20" cy="20" r="18" fill="none" stroke="#1b1714" stroke-width="2"/><path d="M11 20h18M23 14l6 6-6 6" fill="none" stroke="#1b1714" stroke-width="2" stroke-linecap="round" stroke-linejoin="round"/></svg>

  <div class="abs photo blog-img" style="left:99px;top:3044px;background:linear-gradient(180deg,#e9e6e2,#c9bdae 60%,#8c6a4f)" role="img" aria-label="Living room with fireplace and shelves"></div>
  <div class="abs blog-body" style="left:99px;top:3284px"></div>
  <div class="abs date" style="left:131px;top:3263px">06 &nbsp;Nov, 2024</div>
  <div class="abs blog-title" style="left:135px;top:3336px">Lorem ipsum dolor sit amet,<br>consectetur adipiscing</div>
  <div class="abs read" style="left:135px;top:3410px">READ MORE</div>

  <div class="abs photo blog-img" style="left:605px;top:3044px;background:linear-gradient(180deg,#eceae6,#d4c8b8 60%,#b58f68)" role="img" aria-label="Open hallway with wooden staircase and potted tree"></div>
  <div class="abs blog-body" style="left:605px;top:3284px"></div>
  <div class="abs date" style="left:661px;top:3263px">06 &nbsp;Nov, 2024</div>
  <div class="abs blog-title" style="left:665px;top:3336px">Lorem ipsum dolor sit amet,<br>consectetur adipiscing</div>
  <div class="abs read" style="left:665px;top:3410px">READ MORE</div>
</section>

<div class="abs band" style="top:3553px"></div>

<footer class="footer">
  <div class="abs brand" style="left:99px;top:3656px;font-size:40px">DWELLORA</div>
  <svg class="abs" style="left:104px;top:3748px" width="12" height="14" viewBox="0 0 12 14" aria-hidden="true"><path d="M6 13S1 8 1 5a5 5 0 0 1 10 0c0 3-5 8-5 8z" fill="#b98461"/><circle cx="6" cy="5" r="1.8" fill="#f7ede3"/></svg>
  <p class="abs foot-s" style="left:128px;top:3744px;width:250px">"Lorem ipsum dolor sit amet, consectetur adipiscing elit, sed do eiusmod tempor</p>
  <svg class="abs" style="left:104px;top:3800px" width="12" height="12" viewBox="0 0 12 12" aria-hidden="true"><path d="M2 1l2.5 0 1 3-1.5 1a7 7 0 0 0 3 3l1-1.5 3 1V10a1 1 0 0 1-1 1A10 10 0 0 1 1 2a1 1 0 0 1 1-1z" fill="#b98461"/></svg>
  <p class="abs foot-s" style="left:128px;top:3798px">+1 555-010-2040<br>+1 555-010-7731</p>
  <svg class="abs" style="left:104px;top:3855px" width="13" height="10" viewBox="0 0 13 10" aria-hidden="true"><rect width="13" height="10" rx="1" fill="#b98461"/><path d="M1 1l5.5 4.5L12 1" fill="none" stroke="#f7ede3" stroke-width="1.2"/></svg>
  <p class="abs foot-s" style="left:128px;top:3852px">info@dwellora.com</p>

  <div class="abs foot-h" style="left:427px;top:3655px">Quick Links</div>
  <div class="abs link" style="left:428px;top:3713px">Home</div>
  <div class="abs link" style="left:428px;top:3748px">About</div>
  <div class="abs link" style="left:428px;top:3782px">Portfolio</div>
  <div class="abs link" style="left:428px;top:3817px">Inquiry</div>

  <div class="abs foot-h" style="left:674px;top:3655px">Get in Touch With Us</div>
  <div class="abs field" style="top:3706px">Name</div>
  <div class="abs field" style="top:3764px">Email</div>
  <div class="abs field" style="top:3816px">Phone</div>
  <div class="abs btn" style="left:684px;top:3890px;width:132px;height:38px;font-size:14px">SEND NOW</div>

  <div class="abs" style="left:103px;top:3963px;width:964px;height:1.5px;background:var(--gold)"></div>
  <p class="abs foot-s" style="left:105px;top:3993px;font-size:14.5px">Copyright © 2024. Dwellora. All rights reserved.</p>
  <div class="abs social" style="left:892px"></div>
  <div class="abs social" style="left:928px"></div>
  <div class="abs social" style="left:964px"></div>
  <div class="abs social" style="left:1000px"></div>
  <div class="abs social" style="left:1036px"></div>
</footer>
</body>
</html>
```